Ferncrest Dental, LLC business card project

Business card to be designed with current logo.
Dental office- please keep design of card that looks clean and professional.
Please include the following info:
Ferncrest Dental, LLC
Dr. Lorna Pettigrew
2871 Marlowe Street
Bethlehem, PA 18093
610-555-0193
ferncrestdental.office@examplemail.test
Hello everyone-
Reason: Just got back from overseas- will look at all designs and provide feedback. Thank you!
Reason: Polling my friends for the final selection-
thank you to all those that participated- so many talented designers!

```html
<!DOCTYPE html>
<html lang="en">
<head>
<meta charset="utf-8">
<title>Ferncrest Dental, LLC — Business Card</title>
<link rel="stylesheet" href="https://fonts.googleapis.com/css2?family=Source+Sans+3:wght@400&display=swap">
<style>
  :root {
    --backdrop: #c4cccc;
    --card: #ffffff;
    --lime: #93cf1c;
    --lime-soft: #a8d93a;
    --card-edge: #b3bbbb;
  }
  * { margin: 0; padding: 0; box-sizing: border-box; }
  html, body {
    width: 1200px;
    height: 1200px;
    overflow: hidden;
    background: var(--backdrop);
    font-family: "Source Sans 3", "Myriad Pro", sans-serif;
  }
  .canvas {
    position: relative;
    width: 1200px;
    height: 1200px;
  }
  .card {
    position: absolute;
    left: 149px;
    width: 904px;
    height: 517px;
    background: var(--card);
    border: 1px solid var(--card-edge);
  }
  .card--front { top: 40px; }
  .card--back { top: 600px; }

  /* Front */
  .front-brand {
    position: absolute;
    inset: 0;
    display: flex;
    align-items: center;
    justify-content: center;
    gap: 24px;
  }
  .front-brand__dot {
    width: 40px;
    height: 40px;
    border-radius: 50%;
    background: var(--lime);
  }
  .front-brand__name {
    font-size: 84px;
    font-weight: 400;
    color: var(--lime);
    letter-spacing: -1px;
    white-space: nowrap;
  }

  /* Back */
  .back-brand {
    position: absolute;
    left: 33px;
    top: 44px;
    display: flex;
    align-items: center;
    gap: 10px;
  }
  .back-brand__dot {
    width: 16px;
    height: 16px;
    border-radius: 50%;
    background: var(--lime);
  }
  .back-brand__name {
    font-size: 24px;
    color: var(--lime);
    white-space: nowrap;
  }
  .dentist {
    position: absolute;
    left: 0;
    right: 0;
    top: 200px;
    text-align: center;
  }
  .dentist__name {
    font-size: 62px;
    font-weight: 400;
    color: var(--lime);
    line-height: 1.1;
  }
  .dentist__email {
    margin-top: 12px;
    font-size: 27px;
    color: var(--lime);
  }
  .contact-phone {
    position: absolute;
    left: 33px;
    top: 440px;
    font-size: 27px;
    color: var(--lime);
  }
  .contact-address {
    position: absolute;
    left: 595px;
    top: 402px;
    font-size: 27px;
    line-height: 40px;
    color: var(--lime);
    font-style: normal;
  }
</style>
</head>
<body>
  <main class="canvas">
    <section class="card card--front" aria-label="Card front">
      <div class="front-brand">
        <span class="front-brand__dot" aria-hidden="true"></span>
        <h1 class="front-brand__name">Ferncrest Dental, LLC</h1>
      </div>
    </section>

    <section class="card card--back" aria-label="Card back">
      <div class="back-brand">
        <span class="back-brand__dot" aria-hidden="true"></span>
        <span class="back-brand__name">Ferncrest Dental</span>
      </div>
      <div class="dentist">
        <h2 class="dentist__name">Dr. Lorna Pettigrew</h2>
        <p class="dentist__email">ferncrestdental.office@examplemail.test</p>
      </div>
      <p class="contact-phone">(610)555-0193</p>
      <address class="contact-address">2871 Marlowe Street,<br>Bethlehem, PA 18093</address>
    </section>
  </main>
</body>
</html>
```